Bref créative
Quorvant Systems
Professional
Ramesh Tolanimurthy
Chief Executive Officer
27 Sec. 61, Kusum Marg
Bhavanipur, Jaipur
RJ 304417 INDIA
ramesh@quorvant.example
www.quorvant.example
Need business cards and stationery. I am open to design ideas and feedback will be provided timely
Our email address for letterhead/fax is contact@quorvant.example. This should be used in all locations except the business card.
Stationary and envelopes with a watermark would look great !
Use Horizontal Logo provided in files.
www.quorvant.example can also be added few lines below the logo

```html
<!DOCTYPE html>
<html lang="en">
<head>
<meta charset="utf-8">
<title>Quorvant Systems – Stationery Set</title>
<link href="https://fonts.googleapis.com/css2?family=Open+Sans:wght@400;600;700&display=swap" rel="stylesheet">
<style>
:root{
  --stage:#3a3a3a;
  --paper:#ffffff;
  --blue:#2f8fd8;
  --blue-deep:#1b6fb8;
  --blue-light:#8cc6f0;
  --ink:#3c4650;
  --muted:#8a939c;
  --mark:#e6ecf1;
  --caption:#9a9a9a;
  --env-gray:#d9dcdf;
}
*{box-sizing:border-box;margin:0;padding:0}
html,body{width:1200px;height:343px;overflow:hidden;background:var(--stage);font-family:"Open Sans",Arial,sans-serif;color:var(--ink)}
.set{position:relative;width:1200px;height:343px}
.piece{position:absolute;background:var(--paper);overflow:hidden;box-shadow:0 2px 5px rgba(0,0,0,.45)}
.piece svg.swoosh{position:absolute;inset:0;width:100%;height:100%}
.caption{position:absolute;font-size:6px;color:var(--caption);text-align:center;white-space:nowrap}
.brand{display:flex;align-items:center;gap:4px;font-weight:700;color:var(--blue-deep);white-space:nowrap}
.brand .dot{width:10px;height:10px;border-radius:50%;background:var(--blue)}
.watermark{position:absolute;border-radius:50%;background:radial-gradient(circle at 40% 35%,#fff 0%,var(--mark) 70%,#d7dfe6 100%)}
.tiny{font-size:4.5px;line-height:6px;color:var(--muted)}
.contact{position:absolute;font-size:4px;line-height:5.5px;color:var(--ink);white-space:nowrap}
.fax-table{position:absolute;border-collapse:collapse;font-size:4.5px;color:var(--muted)}
.fax-table td{border:1px solid #d5dae0;padding:1px 3px;height:11px;width:50px}
.env-flap{position:absolute;inset:0}
</style>
</head>
<body>
<div class="set">

  <!-- Business card front -->
  <div class="piece card-front" style="left:19px;top:19px;width:130px;height:77px">
    <svg class="swoosh" viewBox="0 0 130 77" preserveAspectRatio="none"><path d="M0 62 Q60 66 130 50 L130 77 L0 77Z" fill="var(--blue)"/><path d="M0 58 Q60 62 130 46" stroke="var(--blue-light)" stroke-width="1.5" fill="none"/></svg>
    <div class="brand" style="position:absolute;left:6px;top:12px;font-size:6px"><span class="dot" style="width:8px;height:8px"></span>Quorvant</div>
    <div class="contact" style="left:56px;top:8px;font-size:3.8px;line-height:5.2px">
      <b>Ramesh Tolanimurthy</b><br>Chief Executive Officer<br>27 Sec. 61, Kusum Marg<br>Bhavanipur, Jaipur<br>RJ 304417 INDIA<br>ramesh@quorvant.example
    </div>
  </div>
  <div class="caption" style="left:19px;top:99px;width:130px">Business Card Front</div>

  <!-- Business card back -->
  <div class="piece card-back" style="left:19px;top:139px;width:130px;height:77px">
    <svg class="swoosh" viewBox="0 0 130 77" preserveAspectRatio="none"><path d="M0 66 Q60 70 130 56 L130 77 L0 77Z" fill="var(--blue)"/></svg>
    <div class="watermark" style="left:45px;top:12px;width:40px;height:40px;background:var(--blue)"></div>
    <div class="brand" style="position:absolute;left:0;right:0;top:54px;justify-content:center;font-size:5px">Quorvant</div>
  </div>
  <div class="caption" style="left:19px;top:219px;width:130px">Business Card Back</div>

  <!-- Business card blue -->
  <div class="piece card-alt" style="left:19px;top:240px;width:130px;height:77px;background:linear-gradient(180deg,var(--blue) 0%,var(--blue-deep) 100%)">
    <div class="watermark" style="left:47px;top:14px;width:36px;height:36px;background:#fff"></div>
    <div class="brand" style="position:absolute;left:0;right:0;top:55px;justify-content:center;font-size:5px;color:#fff">www.quorvant.example</div>
  </div>
  <div class="caption" style="left:19px;top:320px;width:130px">Business Card Alt</div>

  <!-- Letterhead -->
  <div class="piece letterhead" style="left:168px;top:19px;width:216px;height:305px">
    <svg class="swoosh" viewBox="0 0 216 305" preserveAspectRatio="none"><path d="M0 0 L40 0 Q15 10 0 40Z" fill="var(--blue)"/><path d="M216 270 Q150 295 100 305 L216 305Z" fill="var(--blue)"/><path d="M216 262 Q150 290 95 305" stroke="var(--blue-light)" stroke-width="2" fill="none"/></svg>
    <div class="brand" style="position:absolute;left:40px;top:14px;font-size:7px"><span class="dot"></span>Quorvant</div>
    <div class="contact" style="left:104px;top:11px">27 Sec. 61, Kusum Marg<br>Bhavanipur, Jaipur<br>RJ 304417 INDIA</div>
    <div class="contact" style="left:152px;top:11px">contact@quorvant.example<br>www.quorvant.example</div>
    <div class="watermark" style="left:35px;top:95px;width:146px;height:146px"></div>
  </div>
  <div class="caption" style="left:168px;top:327px;width:216px">Letterhead</div>

  <!-- Fax sheet -->
  <div class="piece fax" style="left:408px;top:19px;width:216px;height:305px">
    <svg class="swoosh" viewBox="0 0 216 305" preserveAspectRatio="none"><path d="M0 0 L40 0 Q15 10 0 40Z" fill="var(--blue)"/><path d="M216 270 Q150 295 100 305 L216 305Z" fill="var(--blue)"/><path d="M216 262 Q150 290 95 305" stroke="var(--blue-light)" stroke-width="2" fill="none"/></svg>
    <div class="brand" style="position:absolute;left:40px;top:14px;font-size:7px"><span class="dot"></span>Quorvant</div>
    <div class="contact" style="left:104px;top:11px">27 Sec. 61, Kusum Marg<br>Bhavanipur, Jaipur<br>RJ 304417 INDIA</div>
    <div class="contact" style="left:152px;top:11px">contact@quorvant.example<br>www.quorvant.example</div>
    <table class="fax-table" style="left:8px;top:36px;width:200px">
      <tr><td>To:</td><td></td><td>From:</td><td></td></tr>
      <tr><td>Fax:</td><td></td><td>Phone:</td><td></td></tr>
      <tr><td>Date:</td><td></td><td>Pages:</td><td></td></tr>
    </table>
    <div class="watermark" style="left:35px;top:110px;width:146px;height:146px"></div>
  </div>
  <div class="caption" style="left:408px;top:327px;width:216px">Fax Sheet</div>

  <!-- Compliment slip -->
  <div class="piece slip" style="left:643px;top:19px;width:197px;height:108px">
    <svg class="swoosh" viewBox="0 0 197 108" preserveAspectRatio="none"><path d="M0 0 L35 0 Q12 8 0 30Z" fill="var(--blue)"/><path d="M197 82 Q150 100 110 108 L197 108Z" fill="var(--blue)"/></svg>
    <div class="brand" style="position:absolute;left:0;right:0;top:12px;justify-content:center;font-size:6px"><span class="dot" style="width:8px;height:8px"></span>Quorvant</div>
    <div class="tiny" style="position:absolute;left:0;right:0;top:28px;text-align:center">www.quorvant.example</div>
  </div>
  <div class="caption" style="left:643px;top:130px;width:197px">Compliment Slip</div>

  <div class="piece slip-alt" style="left:643px;top:192px;width:197px;height:120px">
    <svg class="swoosh" viewBox="0 0 197 120" preserveAspectRatio="none"><path d="M0 0 L35 0 Q12 8 0 30Z" fill="var(--blue)"/><path d="M197 92 Q150 112 110 120 L197 120Z" fill="var(--blue)"/></svg>
    <div class="brand" style="position:absolute;left:0;right:0;top:12px;justify-content:center;font-size:6px"><span class="dot" style="width:8px;height:8px"></span>Quorvant</div>
    <div class="contact" style="left:0;right:0;top:28px;text-align:center">27 Sec. 61, Kusum Marg, Bhavanipur, Jaipur RJ 304417</div>
  </div>
  <div class="caption" style="left:643px;top:315px;width:197px">Compliment Slip Alt</div>

  <!-- Envelope back -->
  <div class="piece env-back" style="left:864px;top:19px;width:317px;height:125px;background:var(--env-gray)">
    <svg class="env-flap" viewBox="0 0 317 125" preserveAspectRatio="none" width="317" height="125"><path d="M0 0 L158 70 L317 0Z" fill="#c2c7cc"/><path d="M0 125 L140 60 M317 125 L176 60" stroke="#bfc4c9" stroke-width="1" fill="none"/></svg>
  </div>
  <div class="caption" style="left:864px;top:148px;width:40px">Envelope Back</div>

  <!-- Envelope blue -->
  <div class="piece env-blue" style="left:907px;top:144px;width:274px;height:84px;background:linear-gradient(180deg,var(--blue) 0%,var(--blue-deep) 100%)">
    <svg class="env-flap" viewBox="0 0 274 84" preserveAspectRatio="none" width="274" height="84"><path d="M0 0 L137 46 L274 0Z" fill="#4aa3e4"/></svg>
    <div class="watermark" style="left:128px;top:37px;width:18px;height:18px;background:#fff"></div>
  </div>

  <!-- Envelope front -->
  <div class="piece env-front" style="left:907px;top:228px;width:274px;height:96px">
    <svg class="env-flap" viewBox="0 0 274 96" preserveAspectRatio="none" width="274" height="96"><path d="M0 0 L137 55 L274 0Z" fill="#f1f3f5" stroke="#dde1e5"/></svg>
    <div class="watermark" style="left:128px;top:40px;width:18px;height:18px;background:var(--blue)"></div>
  </div>
  <div class="caption" style="left:907px;top:327px;width:274px">Envelope Front</div>

</div>
</body>
</html>
```